Bright Harbor Theatre Academy Business Card

We need a professional looking card for the Bright Harbor Theatre Academy. The logo is attached.
The owner is: Marla Quintrell
Phone Number: 303-555-0147
Email: bhtheatreacademy@mailbox-example.com
Website: bhtheatre-example.com
Somewhere on the front of the card we would like to see the slogan: Step into the limelight
On the back we would like to see the quote: All the world's a stage. -Edmund Larkwood
We are open to different colors for the wording or maybe just black. Something that will go well with the logo.
Individuals seeking a professional children's theatre.
Business

```html
<!DOCTYPE html>
<html lang="en">
<head>
<meta charset="utf-8">
<title>Bright Harbor Theatre Academy – Business Cards</title>
<link rel="stylesheet" href="https://fonts.googleapis.com/css2?family=Arimo:wght@400&family=Yellowtail&display=swap">
<style>
  :root {
    --ink: #000000;
    --paper: #ffffff;
    --curtain: #6b0202;
    --accent: #6b0000;
    --frame: #1a1a1a;
  }
  html, body {
    margin: 0;
    padding: 0;
    overflow: hidden;
    background: var(--paper);
  }
  .sheet {
    position: relative;
    width: 1200px;
    height: 1047px;
    overflow: hidden;
    background: var(--paper);
    font-family: "Arimo", Arial, sans-serif;
  }
  .sheet-border {
    position: absolute;
    left: 4px; top: 4px;
    width: 1189px; height: 1036px;
    border: 1.5px solid var(--frame);
  }
  .card {
    position: absolute;
    top: 25px;
    width: 549px;
    height: 988px;
    background: var(--ink);
    color: var(--paper);
    text-align: center;
  }
  .card--front { left: 26px; }
  .card--back { left: 626px; }
  .curtain {
    position: absolute;
    left: 167px; top: 82px;
    width: 214px; height: 107px;
    background: var(--curtain);
  }
  .brand-band {
    position: absolute;
    left: 0; top: 217px;
    width: 100%; height: 141px;
    background: var(--paper);
    color: var(--ink);
  }
  .brand-name {
    position: absolute;
    left: 0; right: 0; top: 22px;
    margin: 0;
    font-size: 58px;
    font-weight: 400;
    line-height: 1;
  }
  .brand-sub {
    position: absolute;
    left: 0; right: 0; top: 98px;
    margin: 0;
    font-size: 21px;
    font-weight: 400;
    letter-spacing: 10px;
    line-height: 1;
  }
  .tagline {
    position: absolute;
    left: 0; right: 0; top: 485px;
    margin: 0;
    font-family: "Yellowtail", "Brush Script MT", cursive;
    font-size: 52px;
    font-weight: 400;
    line-height: 1.1;
  }
  .owner {
    position: absolute;
    left: 0; right: 0; top: 663px;
    margin: 0;
    color: var(--accent);
    font-size: 43px;
    font-weight: 400;
    line-height: 1.1;
  }
  .contact {
    position: absolute;
    left: 0; right: 0; top: 816px;
    margin: 0;
    font-style: normal;
    font-size: 22px;
    line-height: 42px;
  }
  .contact-line { display: block; }
  .contact-line--web { color: var(--accent); }
</style>
</head>
<body>
<main class="sheet">
  <div class="sheet-border"></div>

  <section class="card card--front">
    <div class="curtain" role="img" aria-label="Red stage curtain illustration"></div>
    <div class="brand-band">
      <p class="brand-name">Bright Harbor</p>
      <p class="brand-sub">THEATRE ACADEMY</p>
    </div>
    <p class="tagline">Step into the limelight</p>
    <p class="owner">Marla Quintrell</p>
    <address class="contact">
      <span class="contact-line">Phone Number: 303-555-0147</span>
      <span class="contact-line">Email: bhtheatreacademy@mailbox-example.com</span>
      <span class="contact-line contact-line--web">Website: bhtheatre-example.com</span>
    </address>
  </section>

  <section class="card card--back">
    <div class="curtain" role="img" aria-label="Red stage curtain illustration"></div>
    <div class="brand-band">
      <p class="brand-name">Bright Harbor</p>
      <p class="brand-sub">THEATRE ACADEMY</p>
    </div>
    <p class="tagline">All the world's a stage</p>
    <p class="owner">Marla Quintrell</p>
    <address class="contact">
      <span class="contact-line">Phone Number: 303-555-0147</span>
      <span class="contact-line">Email: bhtheatreacademy@mailbox-example.com</span>
      <span class="contact-line contact-line--web">Website: bhtheatre-example.com</span>
    </address>
  </section>
</main>
</body>
</html>
```